Need new to-go sticker labels for my restaurant

I need to go sticker labels that are Modern, eye catching and sleek for sushi restaurant. Or it can be really nostalgic. Please include our logo somehow. It will be printed on a 1" x 2.65" label.

I need to also change each label name and price. Or can you tell me how to change each one or do I send you each label name and price?

Example:

California Roll.
Crab, Avocado, Cucumber
$8.99

Target Market(s)

Health conscious.

Industry/Entity Type

Restaurant

Requirements
Must have
• fresh food appeal. Nostalgia and warmth. Don't make it cookie cutter and just stick balun logo and sushi name, create a picture!! Create something very creative and infuse picture with logo.
Nice to have
• Warmth, nostalgia, fresh looking. Prefer warm tones with fresh appeal. Pick and choose Lime green, red, yellow are fine. Other colors can be used to make exciting!! must catch eye!!! Customers buy WITH THEIR EYES!!!
Should not have
• Should Not be cookie cutter and unnoticed.

```html
<!DOCTYPE html>
<html lang="en">
<head>
<meta charset="utf-8">
<title>Balun Sushi To-Go Label</title>
<link rel="stylesheet" href="https://fonts.googleapis.com/css2?family=Open+Sans:wght@400;700;800&display=swap">
<style>
  :root {
    --backdrop: #000000;
    --label-white: #ffffff;
    --brand-red: #b0001c;
    --brand-red-dark: #7c0010;
    --brand-red-light: #d4202e;
    --lime: #9dc54a;
    --ink: #222222;
    --photo-warm: #e8a27a;
    --photo-cream: #efe4cf;
    --photo-dark: #3c3a33;
  }
  html, body {
    margin: 0;
    padding: 0;
    width: 1200px;
    height: 1000px;
    overflow: hidden;
    background: var(--backdrop);
  }
  .canvas {
    position: relative;
    width: 1200px;
    height: 1000px;
  }
  .label {
    position: absolute;
    left: 465px;
    top: 142px;
    width: 271px;
    height: 714px;
    font-family: "Open Sans", Verdana, sans-serif;
  }
  .label-art {
    position: absolute;
    inset: 0;
    display: block;
  }
  .brand {
    position: absolute;
    left: 0;
    right: 0;
    top: 0;
    text-align: center;
  }
  .brand-mark {
    position: absolute;
    left: 100px;
    top: 70px;
    width: 70px;
    height: 70px;
    background: var(--brand-red);
  }
  .brand-name {
    position: absolute;
    left: 0;
    right: 0;
    top: 186px;
    margin: 0;
    font-size: 46px;
    font-weight: 800;
    letter-spacing: 7px;
    line-height: 1;
    color: var(--brand-red);
    padding-left: 7px;
  }
  .brand-tagline {
    position: absolute;
    left: 0;
    right: 0;
    top: 240px;
    margin: 0;
    font-size: 12px;
    font-weight: 400;
    letter-spacing: 1px;
    color: var(--ink);
  }
  .dish-name {
    font-family: "Open Sans", Verdana, sans-serif;
    font-size: 23px;
    font-weight: 700;
    fill: var(--label-white);
  }
  .dish-details {
    position: absolute;
    left: 0;
    right: 0;
    top: 578px;
    text-align: center;
    color: var(--label-white);
  }
  .dish-price {
    margin: 0;
    font-size: 64px;
    font-weight: 800;
    line-height: 1;
    color: var(--ink);
  }
  .dish-ingredients {
    margin: 2px 0 0;
    font-size: 21px;
    font-weight: 700;
    line-height: 27px;
  }
</style>
</head>
<body>
<div class="canvas">
  <article class="label">
    <svg class="label-art" width="271" height="714" viewBox="0 0 271 714">
      <defs>
        <linearGradient id="top-band-fill" x1="0" y1="0" x2="0" y2="1">
          <stop offset="0" stop-color="var(--brand-red-light)"/>
          <stop offset="1" stop-color="var(--brand-red-dark)"/>
        </linearGradient>
        <linearGradient id="banner-fill" x1="0" y1="0" x2="1" y2="0">
          <stop offset="0" stop-color="var(--brand-red-dark)"/>
          <stop offset="0.5" stop-color="var(--brand-red)"/>
          <stop offset="1" stop-color="var(--brand-red-light)"/>
        </linearGradient>
        <linearGradient id="photo-fill" x1="0" y1="0" x2="1" y2="1">
          <stop offset="0" stop-color="var(--photo-warm)"/>
          <stop offset="0.45" stop-color="var(--photo-cream)"/>
          <stop offset="1" stop-color="var(--photo-dark)"/>
        </linearGradient>
      </defs>
      <rect class="label-base" width="271" height="714" fill="var(--label-white)"/>
      <rect class="top-band" width="271" height="20" fill="url(#top-band-fill)"/>
      <path class="lime-field" d="M0,286 Q135,250 271,280 L271,714 L0,714 Z" fill="var(--lime)"/>
      <path class="sushi-photo" role="img" aria-label="Photo of a sushi platter with salmon nigiri, maki rolls, California rolls and shrimp"
            d="M0,298 Q135,266 271,292 L271,522 L0,530 Z" fill="url(#photo-fill)"/>
      <path class="banner-edge" d="M0,516 Q135,494 271,502 L271,552 Q135,586 0,566 Z" fill="var(--label-white)"/>
      <path class="dish-banner" d="M0,520 Q135,498 271,506 L271,546 Q135,578 0,558 Z" fill="url(#banner-fill)"/>
      <text class="dish-name" x="137" y="550" text-anchor="middle" transform="rotate(-3 137 545)">California Roll</text>
    </svg>

    <header class="brand">
      <span class="brand-mark" aria-hidden="true"></span>
      <h1 class="brand-name">BALUN</h1>
      <p class="brand-tagline">SUSHI &amp; ASIAN CUISINE</p>
    </header>

    <section class="dish-details">
      <p class="dish-price">$8.99</p>
      <p class="dish-ingredients">Crab, Avocado,<br>Cucumber</p>
    </section>
  </article>
</div>
</body>
</html>
```